Want a package created for a new protein bar

We would like a new package created for a new protein bar project The name of the bar will be VOLMBite a real food protein bar, we would like a ‘window’ on the package of bar like Brave Meadow bar below in images.

VOLMBite
‘Super Food Bar’
14g of Whey Protein
The package film size is the following 12cm width x 15cm Length,
Flavor Peanut Chocolate Chip, additional information will be attached shortly like nutrition facts,

Target Market(s)

fitness market, bodybuilders, athletes, everyday people

Industry/Entity Type

Health Product

Logo Text

VOLMBite

Font styles to use
Serif
Sans Serif
Decorative

Requirements
Must have
• Package window

```html
<!DOCTYPE html>
<html lang="en">
<head>
<meta charset="utf-8">
<title>VOLMBite Peanut Wrapper</title>
<link rel="stylesheet" href="https://fonts.googleapis.com/css2?family=Urbanist:wght@300;400;800&family=Anton&display=swap">
<style>
  :root {
    --bg: #ffffff;
    --orange: #f9a10a;
    --ink: #1a1a1a;
    --white: #ffffff;
    --panel: #232323;
    --cream: #f3efe4;
    --nut-light: #c9955a;
    --nut-mid: #a9733f;
    --nut-dark: #6b4322;
    --bar-light: #9a6a3e;
    --bar-dark: #4a2c17;
  }
  html, body {
    margin: 0;
    padding: 0;
    width: 1074px;
    height: 1200px;
    overflow: hidden;
    background: var(--bg);
  }
  .canvas {
    position: relative;
    width: 1074px;
    height: 1200px;
  }
  .wrapper {
    position: absolute;
    left: 87px;
    top: 442px;
    width: 900px;
    height: 315px;
    background: var(--orange);
    overflow: hidden;
    box-shadow: 0 10px 28px rgba(0,0,0,0.22);
    font-family: "Urbanist", sans-serif;
  }
  .brand-name {
    position: absolute;
    left: 31px;
    top: 50px;
    margin: 0;
    font-size: 86px;
    font-weight: 800;
    line-height: 1;
    letter-spacing: -2px;
    color: var(--white);
  }
  .tagline {
    position: absolute;
    left: 41px;
    top: 143px;
    margin: 0;
    font-size: 27px;
    font-weight: 400;
    line-height: 35px;
    color: var(--ink);
  }
  .stat {
    position: absolute;
    top: 240px;
    color: var(--white);
    line-height: 36px;
  }
  .stat-value {
    display: block;
    font-size: 37px;
    font-weight: 800;
  }
  .stat-label {
    display: block;
    font-size: 37px;
    font-weight: 300;
  }
  .stat-calories { left: 41px; }
  .stat-protein { left: 205px; }
  .stat-sugar { left: 366px; }
  .stat-divider {
    position: absolute;
    top: 240px;
    width: 3px;
    height: 75px;
    background: var(--white);
  }
  .divider-one { left: 192px; }
  .divider-two { left: 349px; }
  .flavour-photo {
    position: absolute;
    left: 500px;
    top: 0;
    width: 240px;
    height: 315px;
    background: linear-gradient(90deg, rgba(249,161,10,0) 0%, var(--nut-mid) 30%, var(--nut-light) 60%, var(--nut-dark) 100%);
  }
  .package-window {
    position: absolute;
    left: 588px;
    top: 38px;
    width: 126px;
    height: 240px;
    border: 3px solid var(--cream);
    border-radius: 22px;
    background: linear-gradient(180deg, var(--bar-light) 0%, var(--bar-dark) 100%);
    box-sizing: border-box;
  }
  .flavour-panel {
    position: absolute;
    left: 738px;
    top: 0;
    width: 162px;
    height: 315px;
    background: var(--panel);
    display: flex;
    align-items: center;
    justify-content: center;
  }
  .flavour-name {
    margin: 0;
    writing-mode: vertical-rl;
    font-family: "Anton", sans-serif;
    font-size: 86px;
    line-height: 1;
    letter-spacing: 1px;
    color: var(--cream);
  }
</style>
</head>
<body>
<div class="canvas">
  <div class="wrapper">
    <h1 class="brand-name">VOLMBite</h1>
    <p class="tagline">Super Food Bar<br>Whey Protein</p>

    <div class="stat stat-calories"><span class="stat-value">160</span><span class="stat-label">calories</span></div>
    <span class="stat-divider divider-one"></span>
    <div class="stat stat-protein"><span class="stat-value">14g</span><span class="stat-label">protein</span></div>
    <span class="stat-divider divider-two"></span>
    <div class="stat stat-sugar"><span class="stat-value">2g</span><span class="stat-label">sugar</span></div>

    <div class="flavour-photo" role="img" aria-label="Pile of whole peanuts in their shells"></div>
    <div class="package-window" role="img" aria-label="Clear window showing the protein bar inside"></div>

    <div class="flavour-panel">
      <p class="flavour-name">PEANUT</p>
    </div>
  </div>
</div>
</body>
</html>
```